Studio Vela Hair Artists Business Card

I looking for a updated business card for a hair salon and me as a hairstylist. Something stylish and fun but not to whimsical. There has to be some seriousness about it to attract new clients. Basic imformation will be on the card. An abtract head will be okay but not neccessary. If it will fit, I would love to add my "Merrow Crown Wigs" logo and website (www.merrowcrownwigs.example). The "studio Vela Hair Artists logo is not an official logo, but my signage and some other things use that font. I'm open to an variation of the font and format or keep it as is.

Studio Vela
LORETTA QUINN
OWNER / STYLIST

HAIR RELAZING / STRAIGHTENING
EXTENSIONS / WEAVES
CUTS / CUSTOM COLOR
WIGS

20463 Harlow Bend Way, Suite M
Irvine, CA 92614
(949) 555-0182
Email: studiovelahairartists@studiovelahairartists.example
www.studiovelahairartists.example
Updates

Please eliminate "Merrow Crown Wigs" logo...The focus of the b-card is "Studio Vela Hair Artists." The cards I have received so far has merrow crown wigs center stage. If there was room on the card in a side space, the logo would have been okay, but I don't have to have it on the card. Thanks                                   

Industry/Entity Type

Hair

```html
<!DOCTYPE html>
<html lang="en">
<head>
<meta charset="utf-8">
<title>Studio Vela Hair Artists – Business Card</title>
<link href="https://fonts.googleapis.com/css2?family=Didact+Gothic&family=Arimo:wght@700&display=swap" rel="stylesheet">
<style>
  :root {
    --paper: #ffffff;
    --orange: #ff8300;
    --orange-soft: #ffb45c;
    --maroon: #7a1428;
    --ink: #111111;
    --edge: #e0231c;
  }
  html, body {
    margin: 0;
    padding: 0;
    width: 927px;
    height: 1200px;
    overflow: hidden;
    background: var(--paper);
  }
  .sheet {
    position: relative;
    width: 927px;
    height: 1200px;
  }
  .business-card {
    position: absolute;
    left: 154px;
    width: 637px;
    height: 365px;
    display: block;
  }
  .business-card--light-head { top: 168px; }
  .business-card--maroon-head { top: 687px; }

  .card-base { fill: var(--paper); stroke: var(--edge); stroke-width: 0.8; }
  .card-swoosh { fill: var(--orange); }

  .services, .address, .owner-name, .owner-role, .salon-name {
    font-family: "Didact Gothic", sans-serif;
  }
  .services { fill: var(--ink); font-size: 11px; letter-spacing: 0.2px; }
  .address { fill: var(--ink); font-size: 10.5px; }
  .owner-name, .owner-role { fill: var(--paper); font-size: 15px; letter-spacing: 0.4px; }
  .salon-name { fill: var(--maroon); font-size: 21px; }
  .web-contact {
    font-family: "Arimo", sans-serif;
    font-weight: 700;
    font-size: 9.6px;
    fill: var(--paper);
  }
  .head-art--light { fill: var(--orange-soft); }
  .head-art--maroon { fill: var(--maroon); }
</style>
</head>
<body>
<main class="sheet">

  <svg class="business-card business-card--light-head" viewBox="0 0 412 236" xmlns="http://www.w3.org/2000/svg" aria-label="Business card, light head version">
    <rect class="card-base" x="0.4" y="0.4" width="411.2" height="235.2"/>
    <path class="card-swoosh" d="M270,0 C292,40 282,75 255,95 C222,120 212,130 196,140 C150,170 100,190 0,193 V236 H412 V0 Z"/>
    <g role="img" aria-label="Abstract flowing-hair head illustration in white">
      <ellipse class="head-art--light" cx="350" cy="70" rx="46" ry="62"/>
    </g>
    <text class="services">
      <tspan x="16" y="25">HAIR RELAZING / STRAIGHTENING</tspan>
      <tspan x="16" y="41">EXTENSIONS / WEAVES</tspan>
      <tspan x="16" y="57">CUTS / CUSTOM COLOR</tspan>
      <tspan x="16" y="73">WIGS</tspan>
    </text>
    <text class="salon-name" x="190" y="104" text-anchor="middle">Studio Vela</text>
    <text class="address">
      <tspan x="7" y="144">20463 Harlow Bend Way,</tspan>
      <tspan x="7" y="161">Suite M Irvine, CA 92614</tspan>
      <tspan x="7" y="178">(949) 555-0182</tspan>
    </text>
    <text class="owner-name" x="222" y="152">LORETTA QUINN</text>
    <text class="owner-role" x="222" y="175">OWNER / STYLIST</text>
    <text class="web-contact" x="206" y="211" text-anchor="middle">Email: studiovelahairartists@studiovelahairartists.example</text>
    <text class="web-contact" x="206" y="227" text-anchor="middle">www.studiovelahairartists.example</text>
  </svg>

  <svg class="business-card business-card--maroon-head" viewBox="0 0 412 236" xmlns="http://www.w3.org/2000/svg" aria-label="Business card, maroon head version">
    <rect class="card-base" x="0.4" y="0.4" width="411.2" height="235.2"/>
    <path class="card-swoosh" d="M270,0 C292,40 282,75 255,95 C222,120 212,130 196,140 C150,170 100,190 0,193 V236 H412 V0 Z"/>
    <g role="img" aria-label="Abstract flowing-hair head illustration in maroon">
      <ellipse class="head-art--maroon" cx="350" cy="70" rx="46" ry="62"/>
    </g>
    <text class="services">
      <tspan x="16" y="25">HAIR RELAZING / STRAIGHTENING</tspan>
      <tspan x="16" y="41">EXTENSIONS / WEAVES</tspan>
      <tspan x="16" y="57">CUTS / CUSTOM COLOR</tspan>
      <tspan x="16" y="73">WIGS</tspan>
    </text>
    <text class="salon-name" x="190" y="104" text-anchor="middle">Studio Vela</text>
    <text class="address">
      <tspan x="7" y="144">20463 Harlow Bend Way,</tspan>
      <tspan x="7" y="161">Suite M Irvine, CA 92614</tspan>
      <tspan x="7" y="178">(949) 555-0182</tspan>
    </text>
    <text class="owner-name" x="222" y="152">LORETTA QUINN</text>
    <text class="owner-role" x="222" y="175">OWNER / STYLIST</text>
    <text class="web-contact" x="206" y="211" text-anchor="middle">Email: studiovelahairartists@studiovelahairartists.example</text>
    <text class="web-contact" x="206" y="227" text-anchor="middle">www.studiovelahairartists.example</text>
  </svg>

</main>
</body>
</html>
```